Creative - Appealing - Business Card Design Project

Looking for a Business card design (vector artwork) for an existing company called 'Fernway Sound'. We operate in the entertainment industry specializing in audio system design and rental, however; we also deal with other sectors of the entertainment industry including lighting, video, staging and power system design and rental. We would like to see designs that don't focus too much on audio but include elements encompassing everything else.

Double sided business card, following our new colour scheme and logo, which is attached. The card would ideally be creative and eye catching to draw in new customers in the elegant event production market, such as weddings & corporate affairs.

Target Market(s)

High end corporate clients, wedding clients

Industry/Entity Type

Entertainment

Requirements
Must have
• Our contact details, these can be worded & listed however you think appropriate as part as the design

Business Name - Fernway Sound
My Name - Dominic Harwell
Web Address - www.fernwaysound-example.com
Mobile Number - 07914 362 517
Office Number - 0330 481 7265
Email - dom@fernwaysound-example.com

The name, email and mobile number would need to be able to be changed to my business partners also.

The font used on our logo is Sansation
Nice to have
• On one side maybe a word cloud involving the services in which we can provide; Lighting, Sound, Event Production, Staging, LED Uplighting, Projection Mapping, Wedding Hire

On the other side, all the important credentials of contact.
Should not have
• The design should not use any old style fonts (i.e Times New Roman, Gothic etc) or on the other side of the scale, any 'jokey' fonts (i.e. Comic Sans).

The font to be used is Sansation

```html
<!DOCTYPE html>
<html lang="en">
<head>
<meta charset="utf-8">
<title>Fernway Sound – Business Card</title>
<link rel="stylesheet" href="https://fonts.googleapis.com/css2?family=Exo+2:wght@400;600;700&family=Arimo:wght@400;700&display=swap">
<style>
  :root {
    --purple: #55338f;
    --purple-deep: #4a2a80;
    --purple-soft: #6a4aa3;
    --grey-text: #8a8a8a;
    --grey-light: #b9b9b9;
    --paper: #f7f7f7;
    --stage: #e4e4e6;
    --white: #ffffff;
  }
  * { box-sizing: border-box; margin: 0; padding: 0; }
  html, body { width: 1200px; height: 1000px; overflow: hidden; }
  body {
    background: var(--stage);
    font-family: "Exo 2", "Arimo", sans-serif;
    position: relative;
  }
  .card {
    position: absolute;
    left: 220px;
    width: 760px;
    height: 434px;
    border-radius: 4px;
    box-shadow: 0 6px 18px rgba(0,0,0,0.18);
    overflow: hidden;
  }
  .card--front { top: 48px; background: var(--paper); }
  .card--back { top: 518px; background: var(--purple); }

  /* brand lockup */
  .brand { position: absolute; display: flex; align-items: center; gap: 14px; }
  .brand__mark { width: 26px; height: 26px; }
  .brand__name {
    font-family: "Exo 2", sans-serif;
    font-weight: 700;
    font-size: 42px;
    letter-spacing: 1px;
    text-transform: uppercase;
    line-height: 1;
  }
  .card--front .brand { top: 66px; right: 62px; }
  .card--front .brand__mark { background: var(--purple); }
  .card--front .brand__name { color: var(--grey-light); }

  .holder { position: absolute; left: 62px; bottom: 70px; }
  .holder__name {
    font-family: "Arimo", sans-serif;
    font-weight: 700;
    font-size: 30px;
    color: var(--purple);
    letter-spacing: -0.3px;
  }
  .holder__mobile { margin-top: 8px; }

  .contact {
    font-family: "Arimo", sans-serif;
    font-size: 19px;
    color: var(--grey-text);
    line-height: 1.6;
  }
  .contact__key { color: var(--purple); font-weight: 700; margin-right: 6px; }
  .contact-list { position: absolute; right: 62px; top: 150px; list-style: none; text-align: left; }

  .edge-tab {
    position: absolute; left: 0; bottom: 72px;
    width: 22px; height: 34px; background: var(--purple);
  }

  /* back */
  .word-cloud {
    position: absolute; right: 20px; top: 18px; width: 470px;
    color: var(--purple-soft);
    font-family: "Exo 2", sans-serif;
    font-weight: 600;
    line-height: 1.05;
    opacity: 0.7;
  }
  .word-cloud span { display: inline-block; margin-right: 10px; }
  .wc-lg { font-size: 36px; }
  .wc-md { font-size: 24px; }
  .wc-sm { font-size: 16px; }

  .card--back .brand { left: 62px; top: 150px; }
  .card--back .brand__mark { background: var(--white); }
  .card--back .brand__name { color: var(--white); }
  .web {
    position: absolute; left: 62px; top: 222px;
    font-family: "Arimo", sans-serif; font-weight: 700;
    font-size: 19px; color: var(--white);
  }
  .services {
    position: absolute; left: 470px; top: 170px;
    padding-left: 28px;
    border-left: 1px solid rgba(255,255,255,0.55);
    list-style: none;
    font-family: "Exo 2", sans-serif;
    font-size: 20px; color: var(--white); line-height: 1.55;
  }
  .services__item { display: flex; align-items: center; gap: 12px; }
  .services__bullet { width: 11px; height: 10px; flex: none; }
</style>
</head>
<body>

<section class="card card--front" aria-label="Business card front">
  <div class="brand">
    <span class="brand__mark"></span>
    <span class="brand__name">Fernway Sound</span>
  </div>
  <ul class="contact-list contact">
    <li><span class="contact__key">(o)</span>0330 481 7265</li>
    <li><span class="contact__key">(e)</span>dom@fernwaysound-example.com</li>
    <li><span class="contact__key">(w)</span>www.fernwaysound-example.com</li>
  </ul>
  <div class="holder">
    <div class="holder__name">Dominic Harwell</div>
    <div class="holder__mobile contact"><span class="contact__key">(m)</span>07914 362 517</div>
  </div>
  <span class="edge-tab"></span>
</section>

<section class="card card--back" aria-label="Business card back">
  <div class="word-cloud" aria-hidden="true">
    <span class="wc-md">Lighting</span><span class="wc-sm">Staging</span><span class="wc-lg">Sound</span>
    <span class="wc-sm">Event Production</span><span class="wc-md">LED Uplighting</span>
    <span class="wc-md">Wedding Hire</span><span class="wc-sm">Projection Mapping</span>
    <span class="wc-lg">Sound</span><span class="wc-sm">Lighting</span>
  </div>
  <div class="brand">
    <span class="brand__mark"></span>
    <span class="brand__name">Fernway Sound</span>
  </div>
  <div class="web">www.fernwaysound-example.com</div>
  <ul class="services">
    <li class="services__item"><svg class="services__bullet" viewBox="0 0 11 10"><polygon points="0,0 11,0 5.5,10" fill="none" stroke="#fff" stroke-width="1.4"/></svg>Lighting</li>
    <li class="services__item"><svg class="services__bullet" viewBox="0 0 11 10"><polygon points="0,0 11,0 5.5,10" fill="none" stroke="#fff" stroke-width="1.4"/></svg>Sound</li>
    <li class="services__item"><svg class="services__bullet" viewBox="0 0 11 10"><polygon points="0,0 11,0 5.5,10" fill="none" stroke="#fff" stroke-width="1.4"/></svg>Event Production</li>
    <li class="services__item"><svg class="services__bullet" viewBox="0 0 11 10"><polygon points="0,0 11,0 5.5,10" fill="none" stroke="#fff" stroke-width="1.4"/></svg>Staging</li>
    <li class="services__item"><svg class="services__bullet" viewBox="0 0 11 10"><polygon points="0,0 11,0 5.5,10" fill="none" stroke="#fff" stroke-width="1.4"/></svg>LED Uplighting</li>
    <li class="services__item"><svg class="services__bullet" viewBox="0 0 11 10"><polygon points="0,0 11,0 5.5,10" fill="none" stroke="#fff" stroke-width="1.4"/></svg>Projection Mapping</li>
    <li class="services__item"><svg class="services__bullet" viewBox="0 0 11 10"><polygon points="0,0 11,0 5.5,10" fill="none" stroke="#fff" stroke-width="1.4"/></svg>Wedding Hire</li>
  </ul>
</section>

</body>
</html>
```